Simple and Clean business card design

We would like the design to be simple clean and to incorporate our colors.

We are open to your design and talent, we have the dots in our logo as we think of it as data points and we connect data points for people.

We are open to see the great creative and clean design you bring to the table

Contact Information for Business Card

please include: name, position, email, phone and website

Font styles to use
Sans Serif

Requirements
Must have
• my colors incorporated, simplicity
Nice to have
• lots of white space, simplicity
Should not have
• complexicity/ complex art

```html
<!DOCTYPE html>
<html lang="en">
<head>
<meta charset="utf-8">
<title>Meadowly business card</title>
<link rel="stylesheet" href="https://fonts.googleapis.com/css2?family=Montserrat:wght@400;500;600;700&display=swap">
<style>
  :root {
    --stage: #161616;
    --card: #1d1d1e;
    --ink: #ffffff;
    --muted: #8a8a8a;
    --accent-yellow: #f5be1e;
    --accent-blue: #5a7fc4;
    --accent-green: #34a853;
    --accent-red: #e8453c;
    --soft-grey: #3a3a3a;
  }
  * { box-sizing: border-box; margin: 0; padding: 0; }
  html, body { width: 1200px; height: 909px; overflow: hidden; }
  body {
    background: var(--stage);
    font-family: "Montserrat", sans-serif;
    color: var(--ink);
    position: relative;
  }
  .card {
    position: absolute;
    top: 306px;
    width: 525px;
    height: 300px;
    background: var(--card);
    border-radius: 4px;
    overflow: hidden;
    box-shadow: 0 18px 40px rgba(0,0,0,.55);
  }
  .card--front { left: 50px; }
  .card--back { left: 625px; }

  .card__glow {
    position: absolute;
    background: radial-gradient(circle at 60% 45%, #343434 0%, #262626 45%, rgba(29,29,30,0) 75%);
  }
  .card--front .card__glow { right: -40px; top: 90px; width: 280px; height: 240px; }
  .card--back .card__glow { left: -60px; top: -40px; width: 300px; height: 260px; }

  .wordmark {
    display: flex;
    align-items: center;
    gap: 10px;
    font-weight: 600;
    color: var(--ink);
    letter-spacing: 0.5px;
    position: relative;
  }
  .wordmark__dot {
    border-radius: 50%;
    background: var(--accent-blue);
    flex: none;
  }
  .card--front .wordmark { position: absolute; left: 36px; top: 30px; font-size: 40px; }
  .card--front .wordmark__dot { width: 16px; height: 16px; }

  .person { position: absolute; left: 36px; top: 104px; }
  .person__name { font-size: 20px; font-weight: 600; letter-spacing: 0.5px; }
  .person__first { color: var(--accent-yellow); }
  .person__role { font-size: 15px; font-weight: 400; margin-top: 2px; }

  .contacts { position: absolute; left: 36px; top: 176px; list-style: none; font-size: 13px; }
  .contacts li { display: flex; align-items: center; gap: 9px; margin-bottom: 7px; }
  .contacts svg { width: 12px; height: 12px; flex: none; }

  .address {
    position: absolute;
    left: 290px;
    top: 232px;
    padding-left: 14px;
    border-left: 1.5px solid var(--ink);
    font-size: 13px;
    line-height: 1.45;
  }

  .card--back .wordmark {
    position: absolute;
    left: 0; right: 0; top: 104px;
    justify-content: center;
    font-size: 58px;
  }
  .card--back .wordmark__dot { width: 22px; height: 22px; }
  .card--back .web {
    position: absolute;
    left: 0; right: 0; top: 200px;
    text-align: center;
    font-size: 14px;
    letter-spacing: 5px;
    color: var(--muted);
  }
</style>
</head>
<body>
  <section class="card card--front" aria-label="Business card front">
    <div class="card__glow" role="img" aria-label="Soft grey dot decoration"></div>
    <div class="wordmark">Meadowly<span class="wordmark__dot"></span></div>
    <div class="person">
      <p class="person__name"><span class="person__first">CORIN</span> VALE</p>
      <p class="person__role">Founder/ CEO</p>
    </div>
    <ul class="contacts">
      <li>
        <svg viewBox="0 0 12 12" aria-hidden="true"><path fill="var(--accent-yellow)" d="M2.5 1l2 2.2-1.1 1.2a6 6 0 0 0 4.2 4.2l1.2-1.1 2.2 2-1.3 1.5C5 11 1 7 1 2.3z"/></svg>
        555-014-2290
      </li>
      <li>
        <svg viewBox="0 0 12 12" aria-hidden="true"><rect x="0.5" y="2.5" width="11" height="7" fill="var(--accent-yellow)"/><path d="M0.5 2.5L6 6.5l5.5-4" stroke="var(--card)" fill="none"/></svg>
        corin.vale@meadowly.one
      </li>
      <li>
        <svg viewBox="0 0 12 12" aria-hidden="true"><circle cx="6" cy="6" r="5.2" fill="var(--accent-yellow)"/><path d="M1 6h10M6 1c-2.4 2.8-2.4 7.2 0 10M6 1c2.4 2.8 2.4 7.2 0 10" stroke="var(--card)" stroke-width=".8" fill="none"/></svg>
        www.meadowly.one
      </li>
    </ul>
    <p class="address">18 W. Orchard Lane<br>Larkfield, IL 60000</p>
  </section>

  <section class="card card--back" aria-label="Business card back">
    <div class="card__glow" role="img" aria-label="Soft grey dot decoration"></div>
    <div class="wordmark">Meadowly<span class="wordmark__dot"></span></div>
    <p class="web">www.meadowly.one</p>
  </section>
</body>
</html>
```